Swing Dance Themed Cleaning Company Website

We need a website designed for a cleaning company based in Portland, Oregon called Bellhop Sweep. We clean homes and commercial buildings, inside and out.

needs to be vintage and like the velvet marlow. Speakeasy 1920s feel.
needs to be classy.

Check out bellhopsweep.com We are not happy with the site currently.

please look at house finderly site for more content https://www.housefinderly.com/rated.BellhopSweepCleaning.48217065.html

Check out my videos on my ClipHarbor channel Bellhop Sweep

Target Market(s)

middle class and home owner

Industry/Entity Type

Cleaning Service

Number of Pages Required

3 page

Font styles to use
Other font styles liked:
• jazzrag

Colors

Designer to choose colors to be used in the design.

Requirements
Must have
• must be good on pc and mobile

```html
<!DOCTYPE html>
<html lang="en">
<head>
<meta charset="utf-8">
<title>Bellhop Sweep — Polished Rooms Across Portland</title>
<link rel="stylesheet" href="https://fonts.googleapis.com/css2?family=Poiret+One&family=Montserrat:wght@400;500;700;800&display=swap">
<style>
  :root {
    --gold: #b8893a;
    --gold-bright: #f2d21a;
    --plaque: #b88a3c;
    --ink-dark: #221f20;
    --cocoa: #3a2b29;
    --footer: #7b5214;
    --footer-line: #9a7034;
    --white: #ffffff;
    --muted: #a9a4a2;
    --muted-warm: #c9b9b3;
    --deco: "Poiret One", "Josefin Sans", sans-serif;
    --sans: "Montserrat", "Helvetica Neue", Arial, sans-serif;
  }
  * { margin: 0; padding: 0; box-sizing: border-box; }
  html, body { width: 1200px; height: 2568px; overflow: hidden; background: var(--ink-dark); }
  body { position: relative; font-family: var(--sans); color: var(--white); }
  .abs { position: absolute; }

  /* Hero */
  .hero { position: absolute; left: 0; top: 0; width: 1200px; height: 628px;
    background: radial-gradient(ellipse at 50% 45%, #8a5a2c 0%, #5e3a1c 45%, #2e1d12 100%); }
  .brand { position: absolute; left: 94px; top: 48px; }
  .brand-row { display: flex; align-items: center; gap: 10px; }
  .brand-mark { width: 34px; height: 34px; background: var(--gold-bright); }
  .brand-name { font-family: var(--sans); font-weight: 800; font-size: 27px; line-height: 1; color: var(--gold-bright); letter-spacing: .5px; }
  .brand-tag { margin-top: 10px; font-size: 11px; font-weight: 500; color: var(--gold-bright); letter-spacing: .3px; white-space: nowrap; }
  .nav { position: absolute; right: 98px; top: 68px; display: flex; gap: 28px; align-items: center;
    font-family: var(--deco); font-size: 15px; font-weight: 700; }
  .nav a { color: var(--white); text-decoration: none; }
  .nav a.active { color: var(--gold-bright); }
  .plaque { position: absolute; left: 380px; top: 272px; width: 420px; height: 136px;
    background: var(--plaque); border-radius: 24px; border: 3px solid #d9b36a;
    box-shadow: 0 4px 18px rgba(0,0,0,.45); text-align: center; padding-top: 34px; }
  .plaque h1 { font-family: var(--deco); font-size: 32px; font-weight: 400; letter-spacing: 1px; }
  .plaque p { font-size: 19px; margin-top: 4px; }
  .hero-rule { position: absolute; top: 338px; height: 2px; width: 120px; background: #c9a25a; }
  .dots { position: absolute; z-index: 2; top: 656px; left: 0; width: 1200px; display: flex; justify-content: center; gap: 5px; }
  .dots span { width: 8px; height: 8px; border-radius: 50%; background: var(--white); }
  .dots span.on { background: transparent; border: 1px solid var(--white); }

  /* Section heads */
  .section-head { position: absolute; left: 0; width: 1200px; text-align: center; }
  .section-head h2 { font-family: var(--deco); font-weight: 400; font-size: 34px; letter-spacing: 1px; }
  .section-head p { font-size: 14px; margin-top: 6px; }
  .divider { display: block; margin: 18px auto 0; }

  /* About */
  .about { position: absolute; left: 0; top: 628px; width: 1200px; height: 707px; background: var(--ink-dark); }
  .about-copy { position: absolute; left: 89px; top: 272px; width: 510px; }
  .about-copy h3 { font-family: var(--deco); font-weight: 400; font-size: 35px; color: var(--gold); letter-spacing: .5px; white-space: nowrap; }
  .about-copy h4 { font-size: 26px; font-weight: 400; margin-top: 2px; }
  .about-copy p { font-size: 13.5px; line-height: 22px; color: var(--muted); margin-top: 22px; }
  .actions { display: flex; align-items: center; gap: 34px; margin-top: 26px; }
  .btn { display: inline-block; background: var(--gold); color: var(--white); font-size: 13px; padding: 9px 26px; text-decoration: none; }
  .review { font-size: 12.5px; color: var(--muted-warm); display: flex; align-items: center; gap: 8px; }
  .video { position: absolute; left: 650px; top: 272px; width: 458px; height: 296px; background: #111; }
  .video-frame { width: 458px; height: 266px; background: linear-gradient(120deg, #3c2a22 0%, #6b4a35 45%, #2a1d18 100%); position: relative; }
  .video-title { position: absolute; left: 8px; top: 8px; font-size: 10px; color: #e6e6e6; }
  .video-bar { height: 30px; display: flex; align-items: center; gap: 10px; padding: 0 10px; }
  .track { flex: 1; height: 5px; background: #555; border-radius: 3px; }
  .vtime { font-size: 9px; color: #ddd; }

  /* Quick facts */
  .facts { position: absolute; left: 0; top: 1335px; width: 1200px; height: 639px; background: var(--cocoa); }
  .fact { position: absolute; top: 322px; width: 260px; text-align: center; }
  .fact svg { display: block; margin: 0 auto; }
  .fact h5 { font-size: 22px; font-weight: 400; margin-top: 20px; white-space: nowrap; }
  .fact p { font-size: 11.5px; line-height: 16px; color: var(--muted-warm); margin: 12px auto 0; width: 180px; }

  /* Footer */
  .footer { position: absolute; left: 0; top: 1974px; width: 1200px; height: 594px; background: var(--footer); }
  .screened { position: absolute; left: 142px; top: 80px; }
  .screened h2 { font-family: var(--deco); font-weight: 400; font-size: 27px; letter-spacing: 1px; }
  .screened p { font-size: 12.5px; margin-top: 12px; }
  .badges { position: absolute; left: 656px; top: 78px; display: flex; gap: 30px; }
  .badge { width: 70px; height: 70px; background: #e9e3d6; }
  .badge.round { border-radius: 50%; }
  .footer-rule { position: absolute; left: 98px; top: 204px; width: 1003px; height: 1px; background: var(--footer-line); }
  .foot-brand { position: absolute; left: 116px; top: 274px; }
  .foot-brand .brand-mark { background: var(--white); }
  .foot-brand .brand-name { color: var(--white); }
  .foot-brand .brand-tag { color: var(--white); }
  .copyright { margin-top: 22px; font-size: 13px; }
  .foot-info { position: absolute; left: 426px; top: 272px; width: 280px; }
  .foot-info h6 { font-family: var(--deco); font-weight: 700; font-size: 13px; letter-spacing: .5px; }
  .foot-info p { font-size: 12.5px; line-height: 19px; margin-bottom: 20px; }
  .foot-about { position: absolute; left: 740px; top: 258px; width: 390px; }
  .foot-about h6 { font-family: var(--deco); font-weight: 400; font-size: 18px; letter-spacing: .5px; }
  .foot-about p { font-size: 12.5px; line-height: 20.5px; margin-top: 6px; }
  .socials { display: flex; gap: 10px; margin-top: 20px; font-size: 12px; align-items: center; }
  .socials .sep { width: 1px; height: 12px; background: var(--footer-line); }
</style>
</head>
<body>

<header class="hero" role="img" aria-label="Photo of a cleaner vacuuming a rug in a warm wood-panelled dining room">
  <div class="brand">
    <div class="brand-row"><span class="brand-mark"></span><span class="brand-name">BELLHOP<br>SWEEP</span></div>
    <div class="brand-tag">POLISHED ROOMS ACROSS PORTLAND</div>
  </div>
  <nav class="nav">
    <a href="#">HOME</a><a href="#">CONTACT US</a><a class="active" href="#">ABOUT US</a><a href="#">OUR SERVICES</a><a href="#">BLOG</a>
    <svg width="18" height="18" viewBox="0 0 18 18" fill="none" stroke="#f2d21a" stroke-width="2"><circle cx="7.5" cy="7.5" r="5.5"/><path d="M11.5 11.5L16.5 16.5"/></svg>
  </nav>
  <span class="hero-rule" style="left:240px"></span>
  <span class="hero-rule" style="left:840px"></span>
  <div class="plaque">
    <h1>BELLHOP SWEEP SERVICES</h1>
    <p>Classiest cleaners outdoor indoor</p>
  </div>
  <svg class="abs" style="left:64px;top:326px" width="20" height="32" viewBox="0 0 20 32" fill="none" stroke="#fff" stroke-width="2"><path d="M16 2L4 16L16 30"/></svg>
  <svg class="abs" style="left:1110px;top:326px" width="20" height="32" viewBox="0 0 20 32" fill="none" stroke="#fff" stroke-width="2"><path d="M4 2L16 16L4 30"/></svg>
</header>

<section class="about">
  <div class="section-head" style="top:88px">
    <h2>ABOUT US BELLHOP SWEEP</h2>
    <p>Making the greater Portland area clean, one building at a time</p>
    <svg class="divider" width="400" height="20" viewBox="0 0 400 20" fill="none" stroke="#b8893a" stroke-width="1.5"><path d="M10 10H390"/><circle cx="10" cy="10" r="5"/><circle cx="390" cy="10" r="5"/></svg>
  </div>
  <div class="about-copy">
    <h3>GOOD PEOPLE, GREAT SERVICE</h3>
    <h4>Cleaning and maintenance</h4>
    <p>Bellhop Sweep is a locally owned family business dedicated to providing you with quality cleaning services for a reasonable price. We provide flexible 24 hour service and we are available for cleaning emergencies.Lorem Ipsum is simply dummy text of the printing and typesetting industry. Lorem Ipsum has been the industry's standard dummy text .</p>
    <div class="actions">
      <a class="btn" href="#">Read more</a>
      <span class="review"><svg width="16" height="14" viewBox="0 0 16 14" fill="none" stroke="#c9b9b3" stroke-width="1.2"><path d="M1 6h3v7H1zM4 6l3-5c1.5 0 2 1 1.6 2.4L8 5.5h5.5c1 0 1.6.9 1.3 1.8l-1.6 4.8c-.2.6-.8.9-1.4.9H4"/></svg>Leave a Review</span>
    </div>
  </div>
  <div class="video">
    <div class="video-frame" role="img" aria-label="Promo video still of a cleaner polishing a glass cabinet door">
      <span class="video-title">Bellhop Sweep promo video 30 seconds</span>
    </div>
    <div class="video-bar">
      <svg width="10" height="12" viewBox="0 0 10 12"><path d="M0 0L10 6L0 12Z" fill="#fff"/></svg>
      <span class="track"></span>
      <span class="vtime">00:00</span>
      <svg width="12" height="12" viewBox="0 0 12 12"><path d="M0 4h3l4-3v10L3 8H0Z" fill="#fff"/></svg>
      <span class="track" style="flex:0 0 44px"></span>
      <svg width="10" height="10" viewBox="0 0 10 10" fill="none" stroke="#fff"><rect x="1" y="1" width="8" height="8"/></svg>
    </div>
  </div>
</section>

<div class="dots"><span></span><span class="on"></span><span></span><span></span></div>

<section class="facts">
  <div class="section-head" style="top:108px">
    <h2>BELLHOP SWEEP QUICK FACTS</h2>
    <p>Making the greater Portland area clean, one building at a time</p>
    <svg class="divider" width="400" height="20" viewBox="0 0 400 20" fill="none" stroke="#ffffff" stroke-width="1.5"><path d="M10 10H390"/><circle cx="10" cy="10" r="5"/><circle cx="390" cy="10" r="5"/></svg>
  </div>
  <div class="fact" style="left:80px">
    <svg width="68" height="68" viewBox="0 0 68 68" fill="none" stroke="#c8782e" stroke-width="2"><circle cx="38" cy="30" r="22"/><path d="M38 16V30H48"/><path d="M6 40c4 10 12 18 22 22l6-6-7-6-5 4c-4-2-7-5-9-9l4-5-6-7z"/></svg>
    <h5>Business Hours 24/7</h5>
    <p>We provide cleaning and janitorial services for one-time and recurring needs.</p>
  </div>
  <div class="fact" style="left:367px">
    <svg width="68" height="68" viewBox="0 0 68 68" fill="none" stroke="#c8782e" stroke-width="2"><rect x="6" y="18" width="36" height="30"/><path d="M42 28h12l8 10v10H42z"/><circle cx="18" cy="52" r="5"/><circle cx="52" cy="52" r="5"/></svg>
    <h5>Free Estimates</h5>
    <p>We provide cleaning and janitorial services for one-time and recurring needs.</p>
  </div>
  <div class="fact" style="left:580px">
    <svg width="68" height="68" viewBox="0 0 68 68" fill="none" stroke="#c8782e" stroke-width="2"><circle cx="44" cy="22" r="16"/><rect x="6" y="40" width="30" height="16" fill="#c8782e"/><path d="M36 44h10l6 6v6H36z"/><circle cx="14" cy="60" r="4"/><circle cx="44" cy="60" r="4"/></svg>
    <h5>Trip Charge</h5>
    <p>We provide cleaning and janitorial services for one-time and recurring needs.</p>
  </div>
  <div class="fact" style="left:830px">
    <svg width="68" height="68" viewBox="0 0 68 68" fill="none" stroke="#c8782e" stroke-width="2"><rect x="12" y="14" width="48" height="30" rx="3"/><rect x="6" y="22" width="48" height="30" rx="3" fill="#3a2b29"/><path d="M6 30h48"/></svg>
    <h5>Credit Cards Accepted</h5>
    <p>We provide cleaning and janitorial services for one-time and recurring needs.</p>
  </div>
</section>

<footer class="footer">
  <div class="screened">
    <h2>HOUSE FINDERLY SCREENED &nbsp;APPROVED</h2>
    <p>This service provider has passed the House Finderly screening process.</p>
  </div>
  <div class="badges">
    <span class="badge round"></span><span class="badge"></span><span class="badge"></span><span class="badge"></span>
  </div>
  <div class="footer-rule"></div>
  <div class="foot-brand">
    <div class="brand-row"><span class="brand-mark"></span><span class="brand-name">BELLHOP<br>SWEEP</span></div>
    <div class="brand-tag">POLISHED ROOMS ACROSS PORTLAND</div>
    <div class="copyright">Copyright 2018 Bellhop Sweep</div>
  </div>
  <div class="foot-info">
    <h6>HOURS</h6>
    <p>Thursday - Saturday<br>Dinner: 5:00 pm - 9:30 pm</p>
    <h6>LOCATION</h6>
    <p>418 SE Alder Ct #22, Portland, OR 97214</p>
    <h6>CONTACT</h6>
    <p>971-555-0148<br><span style="font-size:14px">Milo@bellhopsweep.com</span></p>
  </div>
  <div class="foot-about">
    <h6>ABOUT US</h6>
    <p>Bellhop Sweep is a locally owned family business dedicated to providing you with quality cleaning services for a reasonable price. We provide flexible 24 hour service and we are available for cleaning emergencies.Lorem Ipsum is simply dummy text of the printing and typesetting industry. Lorem Ipsum has been the industry's standard dummy text .</p>
    <div class="socials">
      <span>Facelink</span><span class="sep"></span><span>Chirper</span><span class="sep"></span><span>Plusring</span><span class="sep"></span><span>Snapframe</span><span class="sep"></span><span>ClipHarbor</span>
    </div>
  </div>
</footer>

</body>
</html>
```